Business card for Eyelash extension salon in Beverly Hills,California USA

We need new business card for our salon in Beverly Hills. The salon name is 'Lumarra' . We would like to have...Business name: Lumarra Name of person: will provide later Address 6128 N.Corbel Ridge Blvd Corvane Heights , CA 90412 Phone: will provide later (Text only) Web: www.lumarrastudio-example.com Pictogrid icon, Friendvale icon follow us for seasonal campaign and news @lumarrastudioexample Design should look elegant, high-end, clean, simple, cohesive with my brand. Please refer my brand board. Business name color will be metallic bronzy color. Im thinking grey background or white background. Thanks

Target Market(s)

25-35. Gender neutral. People who are in Entertainment business industry.
This is High-end Eyelash extension salon in Beverly Hills

Industry/Entity Type

Beauty Salon

Contact Information for Business Card

Business name: Lumarra
Name of person: will provide later
Address 6128 N.Corbel Ridge Blvd Corvane Heights , CA 90412
Phone: will provide later (Text only)
Web: www.lumarrastudio-example.com
Pictogrid icon, Friendvale icon
follow us for seasonal campaign and news @lumarrastudioexample

Requirements
Must have
• Beautiful, elegant, clean and simple look but very attractive and modern
Should not have
• We don't like too clutter, too busy designs.

```html
<!DOCTYPE html>
<html lang="en">
<head>
<meta charset="utf-8">
<title>Lumarra – Business Card</title>
<link rel="stylesheet" href="https://fonts.googleapis.com/css2?family=Tinos&family=PT+Sans&display=swap">
<style>
  :root {
    --paper: #e6ebea;
    --bronze: #7b5a48;
    --ink: #1c1f1f;
    --frame: #e8c916;
  }
  html, body {
    margin: 0;
    padding: 0;
    overflow: hidden;
    background: var(--paper);
  }
  .card {
    position: relative;
    width: 1200px;
    height: 720px;
    background: var(--paper);
    overflow: hidden;
    font-family: "Tinos", "Times New Roman", serif;
    color: var(--ink);
  }
  .brand-name {
    position: absolute;
    left: 40px;
    top: 80px;
    margin: 0;
    font-family: "Tinos", "Times New Roman", serif;
    font-weight: 400;
    font-size: 124px;
    line-height: 1;
    color: var(--bronze);
  }
  .contact-frame {
    position: absolute;
    left: 115px;
    top: 435px;
    width: 978px;
    height: 262px;
    border: 3px solid var(--frame);
    box-sizing: border-box;
  }
  .icon {
    position: absolute;
    fill: var(--ink);
  }
  .contact-text {
    position: absolute;
    margin: 0;
    font-size: 25.5px;
    line-height: 32px;
    white-space: nowrap;
  }
  .address { left: 226px; top: 460px; }
  .address .line-two { padding-left: 6px; }
  .network-name {
    right: 981px;
    top: 611px;
    font-size: 18px;
  }
  .social-handle { left: 227px; top: 608px; }
  .web {
    left: 714px;
    top: 535px;
    font-size: 24px;
    font-family: "PT Sans", Arial, sans-serif;
  }
  .friendvale { left: 657px; top: 606px; }
</style>
</head>
<body>
<main class="card">
  <h1 class="brand-name">Lumarra</h1>

  <div class="contact-frame"></div>

  <svg class="icon pin-icon" style="left:185px;top:462px" width="26" height="38" viewBox="0 0 26 38" aria-hidden="true">
    <path d="M13 0C5.8 0 0 5.8 0 13c0 9.5 13 25 13 25s13-15.5 13-25C26 5.8 20.2 0 13 0zm0 18a5 5 0 1 1 0-10 5 5 0 0 1 0 10z"/>
  </svg>
  <p class="contact-text address">6128 N.Corbel Ridge Blvd Corvane<br><span class="line-two">Heights , CA 90412</span></p>

  <svg class="icon phone-icon" style="left:183px;top:538px" width="34" height="34" viewBox="0 0 24 24" aria-hidden="true">
    <path d="M6.6 10.8c1.4 2.8 3.8 5.1 6.6 6.6l2.2-2.2c.3-.3.7-.4 1-.2 1.1.4 2.3.6 3.6.6.6 0 1 .4 1 1V20c0 .6-.4 1-1 1C10.6 21 3 13.4 3 4c0-.6.4-1 1-1h3.5c.6 0 1 .4 1 1 0 1.2.2 2.4.6 3.6.1.3 0 .7-.2 1l-2.3 2.2z"/>
  </svg>

  <p class="contact-text network-name">Chirpline</p>
  <p class="contact-text social-handle">@lumarrastudioexample</p>

  <svg class="icon mail-icon" style="left:662px;top:464px" width="36" height="26" viewBox="0 0 36 26" aria-hidden="true">
    <path d="M0 0h36v26H0z M2 3v1l16 11 16-11V3L18 14z M2 7v17l11-9z M34 7v17l-11-9z M4 24h28l-10.5-8.5L18 18l-3.5-2.5z" fill-rule="evenodd"/>
  </svg>

  <svg class="icon globe-icon" style="left:661px;top:532px" width="36" height="36" viewBox="0 0 36 36" aria-hidden="true">
    <circle cx="18" cy="18" r="17"/>
    <g fill="none" stroke="#e6ebea" stroke-width="2.2">
      <ellipse cx="18" cy="18" rx="7" ry="16"/>
      <path d="M2 18h32M5 9h26M5 27h26"/>
    </g>
  </svg>
  <p class="contact-text web">www.lumarrastudio-example.com</p>

  <p class="contact-text friendvale">Friendvale</p>
</main>
</body>
</html>
```